Marke für hochwertige Trauerartikel benötigt Briefpapier
Zielgruppe
Märwind ist eine Marke für hochwertige Trauerartikel. Zielgruppe sind Bestattungsunternehmen, die nachhaltig zufriedenen Kunden möchten.
Aufgabenstellung
Wir benötigen Briefpapier: Anschreiben, Rechnngsformular in Farbe und in schwarz weiß. Dazu Visitenkarten und ein gleicherscheinenden E-Mail Absender. Das Design sollte so klar wir möglich sein. Der Druck erfolgt auf recyceltem Papier.

```html
<!DOCTYPE html>
<html lang="de">
<head>
<meta charset="utf-8">
<title>Märwind – Briefpapier</title>
<link rel="stylesheet" href="https://fonts.googleapis.com/css2?family=Open+Sans:ital,wght@0,400;0,600;0,700;1,700&display=swap">
<style>
  :root {
    --bg: #dcdce0;
    --paper: #f4f5f7;
    --ink: #1c1c1c;
    --muted: #555;
    --gold: #c9a43a;
    --cream: #ece3c8;
    --ornament: #efe6cc;
    --rule: #8a8a8a;
  }
  * { margin: 0; padding: 0; box-sizing: border-box; }
  html, body { width: 1200px; height: 927px; overflow: hidden; }
  body {
    background: var(--bg);
    font-family: "Open Sans", Arial, sans-serif;
    color: var(--ink);
    position: relative;
  }
  .sheet {
    position: absolute;
    width: 305px;
    height: 434px;
    background: var(--paper);
    overflow: hidden;
  }
  .sheet--blank { left: 66px; top: 219px; }
  .sheet--letter { left: 407px; top: 224px; }
  .sheet--invoice { left: 770px; top: 227px; }

  .brand {
    position: absolute;
    display: flex;
    align-items: center;
    gap: 3px;
    font-size: 7px;
    font-weight: 600;
    color: var(--ink);
  }
  .brand__square { width: 6px; height: 6px; background: var(--gold); }

  .ornament-area {
    position: absolute;
    background: radial-gradient(ellipse at 100% 50%, var(--ornament) 0%, rgba(239,230,204,0.55) 55%, rgba(244,245,247,0) 100%);
  }
  .sheet--blank .ornament-area,
  .sheet--letter .ornament-area { left: 166px; top: 74px; width: 139px; height: 312px; border-radius: 156px 0 0 156px; }
  .sheet--invoice .ornament-area {
    left: 45px; top: 323px; width: 235px; height: 111px;
    border-radius: 118px 118px 0 0;
    background: radial-gradient(ellipse at 50% 100%, var(--ornament) 0%, rgba(239,230,204,0.55) 55%, rgba(244,245,247,0) 100%);
  }

  .footer-rule { position: absolute; left: 24px; top: 405px; width: 259px; height: 1.5px; background: var(--rule); }
  .footer-line { position: absolute; left: 24px; top: 409px; font-size: 6.6px; color: var(--muted); letter-spacing: 0.2px; white-space: nowrap; }
  .footer-line .sep { color: var(--gold); margin: 0 2px; }

  .sender { position: absolute; left: 27px; font-size: 5px; line-height: 6.4px; color: var(--ink); }
  .sender--address { top: 93px; }
  .sender--rule { top: 109px; left: 27px; width: 61px; height: 0.6px; background: var(--rule); position: absolute; }
  .sender--contact { top: 112px; }
  .band { position: absolute; top: 427px; height: 7px; }
  .band--gold { left: 0; width: 225px; background: var(--gold); }
  .band--black { left: 228px; width: 77px; background: #000; }

  .invoice-title { position: absolute; left: 29px; top: 53px; font-size: 12.5px; font-weight: 700; letter-spacing: 0.2px; }
  .invoice-title .number { color: var(--gold); margin-left: 4px; }
  .invoice-date { position: absolute; left: 29px; top: 69px; font-size: 6px; }
  .invoice-date b { font-weight: 700; font-size: 6.5px; }
  .issuer { position: absolute; right: 35px; top: 90px; text-align: right; font-size: 5.6px; line-height: 7.5px; color: #333; }
  .client-heading { position: absolute; left: 29px; top: 104px; font-size: 6.2px; font-weight: 700; }
  .client { position: absolute; left: 29px; top: 114px; font-size: 5.6px; line-height: 7.6px; display: grid; grid-template-columns: 31px auto; color: #333; }
  .client dt { font-weight: 600; color: var(--ink); }

  .grid { position: absolute; border-collapse: collapse; font-size: 4.4px; }
  .grid th { background: var(--cream); font-weight: 700; height: 12px; border: 0.8px solid #555; }
  .grid td { border: 0.8px solid #555; height: 11.5px; }
  .grid--units { left: 28px; top: 178px; width: 247px; }
  .grid--items { left: 28px; top: 206px; width: 247px; }
  .grid--totals { left: 233px; top: 275px; width: 42px; }
  .grid--totals td { height: 12.5px; border-color: #777; }

  .comment-box { position: absolute; left: 27px; top: 277px; width: 127px; height: 36px; border: 0.8px solid #555; }
  .comment-box__head { background: var(--cream); height: 12px; font-size: 5.6px; font-weight: 700; padding: 2px 0 0 8px; border-bottom: 0.8px solid #555; }
  .total-label { position: absolute; left: 197px; top: 302px; font-size: 7.5px; font-weight: 700; }
  .thanks { position: absolute; left: 28px; top: 384px; font-size: 5.8px; font-weight: 700; font-style: italic; }
</style>
</head>
<body>

  <section class="sheet sheet--blank" aria-label="Briefbogen Folgeseite">
    <div class="brand" style="left:27px; top:66px;"><span class="brand__square"></span>Märwind</div>
    <div class="ornament-area" role="img" aria-label="Zartes florales Linienornament in Creme"></div>
    <div class="footer-rule"></div>
    <p class="footer-line">Lindenweg 12 PLZ 2210<span class="sep">|</span>Postfach: 40218377<span class="sep">|</span>Fon: 71234560<span class="sep">|</span>Fax: 7654321</p>
  </section>

  <section class="sheet sheet--letter" aria-label="Briefbogen Anschreiben">
    <div class="brand" style="left:29px; top:62px;"><span class="brand__square"></span>Märwind</div>
    <p class="sender sender--address">14 Birkenallee<br>Nordhain 2210</p>
    <div class="sender--rule"></div>
    <p class="sender sender--contact">Tél: +49 521 440 180<br>Email: post@maerwind.de<br>Website: www.maerwind.de</p>
    <div class="ornament-area" role="img" aria-label="Zartes florales Linienornament in Creme"></div>
    <div class="band band--gold"></div>
    <div class="band band--black"></div>
  </section>

  <section class="sheet sheet--invoice" aria-label="Rechnungsformular">
    <h1 class="invoice-title">INVOICE<span class="number">1345</span></h1>
    <p class="invoice-date"><b>Date:</b> 31 nov, 2020</p>
    <div class="brand" style="left:236px; top:55px;"><span class="brand__square"></span>Märwind</div>
    <p class="issuer">14 Birkenallee<br>Nordhain 2210<br>Tél: +49 521 440 181<br>Email: buero@maerwind.de<br>Website: www.maerwind.de</p>

    <p class="client-heading">FACTURE A LINTENTION DE:</p>
    <dl class="client">
      <dt>NOM:</dt><dd>Nom de la societé</dd>
      <dt>ADRESSE:</dt><dd>Contact, Helga eemple<br>adresse Eemple adresse</dd>
      <dt>TEL:</dt><dd>521 44 000 000</dd>
      <dt>EMAIL:</dt><dd>kunde@postfach.de</dd>
    </dl>

    <table class="grid grid--units">
      <tr><th style="width:36px">Description</th><th style="width:52px">Unité</th><th style="width:37px">Quantité</th><th style="width:37px">Montant</th><th style="width:44px">Prix ttc</th><th>Totale</th></tr>
      <tr><td></td><td></td><td></td><td></td><td></td><td></td></tr>
    </table>

    <table class="grid grid--items">
      <tr><th style="width:88px">Description</th><th style="width:37px">Quantité</th><th style="width:37px">Montant</th><th style="width:44px">Prix ttc</th><th>Totale</th></tr>
      <tr><td></td><td></td><td></td><td></td><td></td></tr>
      <tr><td></td><td></td><td></td><td></td><td></td></tr>
      <tr><td></td><td></td><td></td><td></td><td></td></tr>
      <tr><td></td><td></td><td></td><td></td><td></td></tr>
    </table>

    <table class="grid grid--totals">
      <tr><td></td></tr><tr><td></td></tr><tr><td></td></tr>
    </table>

    <div class="comment-box"><p class="comment-box__head">Other comment or other instruction</p></div>
    <p class="total-label">Totale</p>

    <div class="ornament-area" role="img" aria-label="Zartes florales Linienornament in Creme"></div>
    <p class="thanks">THANK YOU FOR YOUR BUSINESS!</p>
  </section>

</body>
</html>
```